Business Card desgin, company called Stand Fast.

I am looking for the logo colors (3) to be used on the card in whatever design you think might work. the certifications are on the back (4) on the front will be my name, Dana Whitlock, owner/instructor, phone 208.555.0193, website www.sfx-drills.example, email dw@sfx-drills.example. im flexible on fonts.

Target Market(s)

firearms owners

Industry/Entity Type

firearms training

Contact Information for Business Card

certification icons on back

```html
<!DOCTYPE html>
<html lang="en">
<head>
<meta charset="utf-8">
<title>Stand Fast – Business Card</title>
<link href="https://fonts.googleapis.com/css2?family=Montserrat:wght@400;500;700&display=swap" rel="stylesheet">
<style>
  :root {
    --backdrop: #2b2b2d;
    --navy: #133257;
    --navy-deep: #0d2746;
    --red: #c21d2f;
    --white: #f4f4f4;
    --orange: #ef7a22;
    --charcoal: #2c2c30;
    --sky: #5aa0d8;
    --gold: #e8a53a;
  }
  * { box-sizing: border-box; margin: 0; padding: 0; }
  html, body { width: 1200px; height: 689px; overflow: hidden; }
  body {
    background: var(--backdrop);
    font-family: "Montserrat", sans-serif;
    position: relative;
  }
  .card {
    position: absolute;
    width: 520px;
    height: 297px;
    border-radius: 18px;
    overflow: hidden;
    top: 196px;
  }
  /* Back side */
  .card-back { left: 50px; background: var(--navy); }
  .back-ring {
    position: absolute;
    left: 36px; top: 46px;
    width: 200px; height: 200px; border-radius: 50%;
    border: 18px solid var(--white);
  }
  .back-brand-name {
    position: absolute;
    left: 262px; top: 218px;
    color: var(--white);
    font-weight: 700;
    font-size: 26px;
    letter-spacing: 1px;
    text-transform: uppercase;
    white-space: nowrap;
    line-height: 1;
  }
  .badges {
    position: absolute;
    left: 300px; top: 22px;
    width: 190px; height: 170px;
  }
  .badge { position: absolute; }
  .badge-orange { left: 0; top: 34px; }
  .badge-shield { left: 100px; top: 0; }
  .badge-blue { left: 34px; top: 108px; }
  .badge-gold { left: 110px; top: 78px; }

  /* Front side */
  .card-front { left: 630px; background: var(--navy-deep); }
  .front-brand {
    position: absolute;
    left: 38px; top: 62px;
    width: 170px;
    text-align: center;
  }
  .front-brand .brand-name {
    color: var(--red);
    font-weight: 700;
    font-size: 21px;
    letter-spacing: 1px;
    text-transform: uppercase;
  }
  .front-brand .ring {
    margin: 14px auto 0;
    width: 120px; height: 120px; border-radius: 50%;
    border: 11px solid var(--white);
  }
  .divider {
    position: absolute;
    left: 232px; top: 40px;
    width: 1px; height: 170px;
    background: rgba(255,255,255,0.25);
  }
  .details {
    position: absolute;
    left: 256px; top: 58px;
    color: var(--white);
  }
  .details .person-name {
    color: var(--red);
    font-weight: 700;
    font-size: 22px;
    text-transform: uppercase;
    letter-spacing: 0.5px;
  }
  .details .role { font-size: 15px; margin-top: 2px; }
  .contact-list { list-style: none; margin-top: 20px; font-size: 13px; }
  .contact-list li { display: flex; align-items: center; gap: 8px; line-height: 1.5; }
  .contact-list svg { width: 12px; height: 12px; flex: none; }
  .stripe-thin {
    position: absolute; left: 0; right: 0; bottom: 34px;
    height: 4px; background: var(--red);
  }
  .stripe-band {
    position: absolute; left: 0; right: 0; bottom: 0;
    height: 26px; background: var(--red);
  }
  .corner-ring {
    position: absolute; right: 22px; bottom: 20px;
    width: 40px; height: 40px; border-radius: 50%;
    background: var(--navy-deep);
    border: 4px solid var(--white);
  }
</style>
</head>
<body>
  <section class="card card-back" aria-label="Card back">
    <div class="back-ring"></div>
    <div class="back-brand-name">Stand Fast</div>
    <div class="badges" aria-label="Certification badges">
      <svg class="badge badge-orange" width="68" height="66" viewBox="0 0 68 66">
        <path d="M34 2 L64 12 L60 44 L34 64 L8 44 L4 12 Z" fill="var(--orange)" stroke="var(--white)" stroke-width="4"/>
      </svg>
      <svg class="badge badge-shield" width="76" height="62" viewBox="0 0 76 62">
        <path d="M38 2 L70 10 L64 42 L38 60 L12 42 L6 10 Z" fill="var(--white)" stroke="var(--red)" stroke-width="4"/>
      </svg>
      <svg class="badge badge-blue" width="74" height="58" viewBox="0 0 74 58">
        <path d="M6 4 H58 L70 29 L58 54 H6 Z" fill="var(--charcoal)" stroke="var(--sky)" stroke-width="3"/>
      </svg>
      <svg class="badge badge-gold" width="74" height="58" viewBox="0 0 74 58">
        <path d="M6 4 H58 L70 29 L58 54 H6 Z" fill="var(--charcoal)" stroke="var(--gold)" stroke-width="3"/>
      </svg>
    </div>
  </section>

  <section class="card card-front" aria-label="Card front">
    <div class="front-brand">
      <div class="brand-name">Stand Fast</div>
      <div class="ring"></div>
    </div>
    <div class="divider"></div>
    <div class="details">
      <div class="person-name">Dana Whitlock</div>
      <div class="role">Owner/Instructor</div>
      <ul class="contact-list">
        <li><svg viewBox="0 0 12 12"><path d="M3 1 L5 3 L4 5 C5 7 6 8 7 8 L9 7 L11 9 L9 11 C5 11 1 7 1 3 Z" fill="var(--red)"/></svg>208.555.0193</li>
        <li><svg viewBox="0 0 12 12"><rect x="1" y="2.5" width="10" height="7" fill="var(--red)"/><path d="M1 2.5 L6 6.5 L11 2.5" fill="none" stroke="var(--navy-deep)" stroke-width="1"/></svg>dw@sfx-drills.example</li>
        <li><svg viewBox="0 0 12 12"><circle cx="6" cy="6" r="5" fill="none" stroke="var(--red)" stroke-width="1.2"/><path d="M1 6 H11 M6 1 V11 M3.5 2 Q6 6 3.5 10 M8.5 2 Q6 6 8.5 10" fill="none" stroke="var(--red)" stroke-width="0.8"/></svg>www.sfx-drills.example</li>
        <li><svg viewBox="0 0 12 12"></svg>www.sfx-drills.example.im</li>
      </ul>
    </div>
    <div class="stripe-thin"></div>
    <div class="stripe-band"></div>
    <div class="corner-ring"></div>
  </section>
</body>
</html>
```